Real Estate Development and Brokerage Middle East

Required is a web site design for a new branch of an existing Real Estate Development and Brokerage company. The Branch will be established in the United Arab Emirates - Veluna Middle East, the mother company is based in Austria/Europe. The new branch focuses on the middle eastern clients such as Institutional Investors/Family Businesses/Wealthy Individuals looking either for a luxury home in Vienna City or the alpine nature or are interested to invest in ready made properties or real estate development projects in Austria run by the branches mother co. in Austria. The design should highlight both Services i.e. Investment for commercial purpose and for residential purposes (focus on the nature) as well as the companies focus on high end luxury selected properties only and having middle east experienced staff in the UAE.

The link to the Austrian HQ website is below: Design elements of that website might or might not be used, however the logo shall be the same.
http://plenodraft.example/QW7RTZMBX

Attached the logo and a rough first draft of the structure of the website (not yet set in stone) . The attachment contains also a link to a website of a company in a similar industry. I do like the way they present the highlights on their start/home page. The boxes. By the way, we believe that more graphic (pictures) and a bit less text might be a good way to approach our future target customers.

As we hope to sell many of the projects and hence many new projects descriptions/pictures will be uploaded in future on an ongoing basis the page should have the ability to upload information and pics by our team (none of it is a web designer and has experience exceeding MS-Office).

Lastly - and for the future we might need (not sure yet) need the entire context in Arabic (the language button)

Thanks.
Lars

Target Market(s)

Institutional Investors and wealthy individuals / family offices

Industry/Entity Type

Real Estate

Coding

Number of Pages Required

5+ page

Requirements
Must have
• Same Logo as Parent Company
Nice to have
• News ticker/banner, high resolution picture heavy, changing pictures on start/home page, PDF downloads

```html
<!DOCTYPE html>
<html lang="en">
<head>
<meta charset="utf-8">
<title>Veluna Immobilien</title>
<link rel="stylesheet" href="https://fonts.googleapis.com/css2?family=Teko:wght@400;500&family=Signika:wght@400;600&family=Dancing+Script:wght@700&family=Open+Sans:wght@400;600;700&display=swap">
<style>
:root{
  --steel:#5f8aa5;
  --steel-dark:#2f4f62;
  --nav-active:#5b88a6;
  --ink:#1d1d1d;
  --body:#333;
  --pale:#e2f0f8;
  --bubble:#a9c8da;
  --footer:#0c2633;
  --footer-box:#0a1e28;
  --accent:#2e9bd0;
  --bar:#5e88a2;
  --white:#fff;
}
*{margin:0;padding:0;box-sizing:border-box}
html,body{width:778px;height:1200px;overflow:hidden;background:#fff}
body{position:relative;font-family:Arial,Helvetica,sans-serif;color:var(--body)}
.hero{position:absolute;left:0;top:0;width:778px;height:344px;background:linear-gradient(160deg,#b8d4ea 0%,#6f9cc4 30%,#4e7396 55%,#8e8f8c 80%,#5d6060 100%)}
.sidebar{position:absolute;left:65px;top:0;width:156px;height:344px;background:rgba(244,246,248,.93)}
.brand{position:absolute;left:0;top:20px;width:156px;text-align:center}
.brand-mark{display:block;width:34px;height:34px;margin:0 auto 12px;border-radius:50%;background:var(--steel)}
.brand-name{font-family:'Open Sans',sans-serif;font-size:14px;font-weight:400;color:var(--steel-dark);letter-spacing:.3px}
.nav{position:absolute;left:18px;top:121px;list-style:none}
.nav li{width:116px;height:18px;margin-bottom:10.5px;padding-left:10px;font-family:'Teko',sans-serif;font-size:15px;line-height:21px;letter-spacing:.6px;color:#333}
.nav li.active{background:var(--nav-active);color:#fff}
.search-bar{position:absolute;left:0;top:344px;width:778px;height:54px;background:var(--steel);border-top:3px solid #9fbccd}
.search-label{position:absolute;left:68px;top:15px;font-family:'Signika',sans-serif;font-weight:600;font-size:16px;color:#1f3442}
.select{position:absolute;top:17px;height:23px;background:#fff;border:1px solid #c9d3da;font-size:9px;color:#777;padding:6px 0 0 5px}
.select::after{content:"";position:absolute;right:5px;top:5px;width:10px;height:10px;border:1px solid #555;background:linear-gradient(#fff,#ddd)}
.select::before{content:"";position:absolute;right:8px;top:9px;border:2px solid transparent;border-top:3px solid #333;z-index:1}
.btn-search{position:absolute;left:627px;top:16px;width:80px;height:26px;background:var(--steel-dark);color:#fff;font-family:'Open Sans',sans-serif;font-size:11px;letter-spacing:.8px;text-align:center;line-height:26px}
.welcome{position:absolute;left:66px;top:424px;width:446px}
.welcome h1{font-family:'Teko',sans-serif;font-weight:400;font-size:26px;color:var(--ink);margin-bottom:6px;letter-spacing:.2px}
.welcome p{font-size:8.7px;line-height:13px;margin-bottom:12px}
.quote{position:absolute;left:543px;top:429px;width:170px;height:184px;background:var(--bubble);border-radius:10px}
.quote-tail{position:absolute;left:688px;top:610px}
.quote-title{font-family:'Dancing Script',cursive;font-size:13px;line-height:16.5px;color:#233541;padding:4px 12px 6px;border-bottom:1px solid #dfeaf1}
.quote-text{font-size:7.9px;line-height:13px;color:#222;text-align:justify;padding:9px 12px 0}
.author{position:absolute;left:558px;top:629px;font-size:7.4px;line-height:15px;color:#444}
.author b{color:#222}
.avatar{position:absolute;left:661px;top:631px;width:26px;height:26px;border-radius:50%;background:linear-gradient(#d8d8d8,#9a9a9a);border:2px solid #eee}
.showcase{position:absolute;left:0;top:694px;width:778px;height:249px;background:var(--pale)}
.card{position:absolute;top:41px;width:147px}
.card-photo{width:147px;height:106px;border:3px solid #fff;box-shadow:0 0 2px rgba(0,0,0,.25);position:relative}
.card-tools{position:absolute;left:44px;bottom:4px;display:flex;gap:3px}
.card-tools span{width:15px;height:15px;border-radius:50%;background:#2a2a2a;border:1.5px solid #fff}
.card p{font-size:8.2px;line-height:13px;margin:15px 5px 0}
.card .more{font-weight:bold;font-size:8.5px;color:#333;margin-top:3px}
.arrow-btn{position:absolute;top:771px;width:20px;height:28px;background:#fff;border-radius:50%;opacity:.85}
.footer{position:absolute;left:0;top:943px;width:778px;height:235px;background:var(--footer);font-family:'Open Sans',sans-serif}
.footer h2{position:absolute;top:16px;font-family:'Open Sans',sans-serif;font-weight:400;font-size:15px;color:var(--accent)}
.feat{position:absolute;left:82px;width:175px;height:48px;background:var(--footer-box)}
.feat-photo{position:absolute;left:0;top:0;width:65px;height:48px}
.feat-info{position:absolute;left:71px;top:6px;font-size:7.5px;line-height:11px;color:#fff}
.feat-info .addr{color:var(--accent);font-weight:700;font-size:8.5px}
.feat-info .price{font-weight:700}
.contact-row{position:absolute;left:298px;font-size:8.8px;line-height:13px;color:#fff}
.contact-row .lbl{position:absolute;left:18px;color:var(--accent);font-weight:600;width:40px;text-align:right}
.contact-row .val{position:absolute;left:64px;white-space:nowrap}
.contact-row svg{position:absolute;left:0;top:1px}
.form-label{position:absolute;left:503px;font-size:8.8px;font-weight:700;color:#fff}
.form-label em{color:#e0403c;font-style:normal}
.field{position:absolute;left:503px;width:175px;background:#fff}
.btn-send{position:absolute;left:628px;top:1142px;width:50px;height:21px;background:var(--accent);color:#fff;font-size:9px;line-height:21px;padding-left:11px;font-family:'Open Sans',sans-serif}
.bottom-bar{position:absolute;left:0;top:1178px;width:778px;height:22px;background:var(--bar);font-size:8.5px;color:#fff;line-height:22px;padding-left:76px}
.social{position:absolute;right:100px;top:6px;display:flex;gap:11px}
.social span{width:10px;height:10px;border-radius:50%;background:#fff;opacity:.9}
</style>
</head>
<body>

<div class="hero" role="img" aria-label="Upward view of a curved glass office tower against a bright sky with clouds"></div>
<aside class="sidebar">
  <div class="brand">
    <span class="brand-mark"></span>
    <div class="brand-name">Veluna Immobilien</div>
  </div>
  <ul class="nav">
    <li class="active">HOME</li>
    <li>ABOUT US</li>
    <li>PROPERTIES</li>
    <li>SERVICES &amp; NEWS</li>
    <li>REFERENCES</li>
    <li>CONTACT</li>
  </ul>
</aside>

<section class="search-bar">
  <div class="search-label">Quick Search:</div>
  <div class="select" style="left:171px;width:107px">Property type</div>
  <div class="select" style="left:294px;width:104px">Location</div>
  <div class="select" style="left:418px;width:89px">Min Price</div>
  <div class="select" style="left:522px;width:88px">Max Price</div>
  <div class="btn-search">SEARCH</div>
</section>

<section class="welcome">
  <h1>Welcome to Veluna</h1>
  <p>Lorem ipsum dolor sit amet, consectetur adipiscing elit etiam accumsan, ipsum a tristique varius non euismod elit massa vitae odio. Vestibulum sodales nisi quis nisi imperdiet scelerisque euismod ulum elit odio, eu porta metus aenean Lorem ipsum dolor sit amet, consectetur adipiscing elit etiam accumsan, ipsum a tristique varius non euismod elit massa vitae odio. Vestibulum sodales nisi quis nisi imperdiet scelerisque euismod ulum elit odio, eu porta metus aenean posuere hendrerit lacus sit amet venenatis. posuere hendrerit lacus sit amet venenatis.Lorem ipsum dolor sit amet, consectetur adipiscing elit etiam accumsan.quis nisi imperdiet scelerisque euismod ulum elit odio.</p>
  <p>Vestibulum sodales nisi quis nisi imperdiet scelerisque euismod ulum elit odio, eu porta metus aenean Lorem ipsum dolor sit amet, consectetur adipiscing elit etiam accumsan, ipsum a tristique varius non euismod elit massa vitae odio. Vestibulum sodales nisi quis nisi imperdiet scelerisque euismod.</p>
</section>

<div class="quote">
  <div class="quote-title">Dorian Holt, Principal, Holt &amp; Partners, Canada</div>
  <div class="quote-text">“Mirela’s consistency and high quality of work is a great support to my business. The confidence of knowing that she will deliver what is needed on time enables me to work on other aspects of the business resulting in better outcomes for my clients.”</div>
</div>
<svg class="quote-tail" width="26" height="16" viewBox="0 0 26 16"><path d="M0 0H25V3Q16 10 0 16Z" fill="var(--bubble)"/></svg>
<div class="author">Owen T. Marsh - USA<br><b>Northvale Corp.</b></div>
<div class="avatar" role="img" aria-label="Client portrait"></div>

<section class="showcase">
  <div class="card" style="left:67px">
    <div class="card-photo" role="img" aria-label="Mediterranean villa with pool at dusk" style="background:linear-gradient(#6f9cd6,#a89a80 55%,#3a6e8a)"><div class="card-tools"><span></span><span></span><span></span></div></div>
    <p>Lorem Ipsum is simply dummy text of the pring and typesetting</p><p class="more">More info &gt;&gt;</p>
  </div>
  <div class="card" style="left:230px">
    <div class="card-photo" role="img" aria-label="Stone mansion with palm trees and driveway" style="background:linear-gradient(#7ea6d4,#b2a07a 55%,#8c8a7e)"><div class="card-tools"><span></span><span></span><span></span></div></div>
    <p>Lorem Ipsum is simply dummy text of the pring and typesetting</p><p class="more">More info &gt;&gt;</p>
  </div>
  <div class="card" style="left:392px">
    <div class="card-photo" role="img" aria-label="Large grey house with turquoise pool" style="background:linear-gradient(#4a6fa8,#8a8e98 50%,#3bb3c4)"><div class="card-tools"><span></span><span></span><span></span></div></div>
    <p>Lorem Ipsum is simply dummy text of the pring and typesetting</p><p class="more">More info &gt;&gt;</p>
  </div>
  <div class="card" style="left:555px">
    <div class="card-photo" role="img" aria-label="Modern villa lit up at twilight" style="background:linear-gradient(#3f6fc2,#b68f8a 55%,#7a7a6a)"><div class="card-tools"><span></span><span></span><span></span></div></div>
    <p>Lorem Ipsum is simply dummy text of the pring and typesetting</p><p class="more">More info &gt;&gt;</p>
  </div>
</section>
<div class="arrow-btn" style="left:56px"><svg width="20" height="28"><path d="M11 9L7 14L11 19" stroke="#999" fill="none"/></svg></div>
<div class="arrow-btn" style="left:688px"><svg width="20" height="28"><path d="M9 9L13 14L9 19" stroke="#999" fill="none"/></svg></div>

<footer class="footer">
  <h2 style="left:82px">Featured</h2>
  <h2 style="left:296px">Contact</h2>
  <h2 style="left:503px">Say Hello!</h2>

  <div class="feat" style="top:59px">
    <div class="feat-photo" role="img" aria-label="Modern kitchen interior" style="background:linear-gradient(90deg,#6a6f74,#c9ccd0)"></div>
    <div class="feat-info"><div class="addr">3412 Cedar Ridge Dr</div>Fairhill, SA<div class="price">249000 €</div></div>
  </div>
  <div class="feat" style="top:115px">
    <div class="feat-photo" role="img" aria-label="Bright open-plan living room" style="background:linear-gradient(90deg,#b59a74,#eee8dc)"></div>
    <div class="feat-info"><div class="addr">1030 Linden Ave</div>Oakmere, SA<div class="price">486000 €</div></div>
  </div>

  <div class="contact-row" style="top:59px">
    <svg width="9" height="11" viewBox="0 0 9 11"><path d="M4.5 0A4 4 0 0 0 .5 4C.5 7 4.5 11 4.5 11S8.5 7 8.5 4A4 4 0 0 0 4.5 0Z" fill="#fff"/><circle cx="4.5" cy="4" r="1.5" fill="var(--footer)"/></svg>
    <span class="lbl">Address:</span><span class="val">250 Harbor Lane<br>Brookfield, CA 90000<br>United States</span>
  </div>
  <div class="contact-row" style="top:107px">
    <svg width="10" height="10" viewBox="0 0 10 10"><path d="M2 0L4 2.5L3 4Q4.5 6.5 6 7L7.5 6L10 8L8.5 10Q2 9 0 1.5Z" fill="#fff"/></svg>
    <span class="lbl">Phone:</span><span class="val">+00 123 456 000</span>
  </div>
  <div class="contact-row" style="top:130px">
    <svg width="11" height="8" viewBox="0 0 11 8"><rect width="11" height="8" fill="#fff"/><path d="M0 0L5.5 4.5L11 0" stroke="var(--footer)" fill="none"/></svg>
    <span class="lbl">E-mail:</span><span class="val">info@veluna.example</span>
  </div>
  <div class="contact-row" style="top:153px">
    <svg width="10" height="10" viewBox="0 0 10 10"><circle cx="5" cy="5" r="5" fill="#fff"/></svg>
    <span class="lbl">Skype:</span><span class="val">veluna.office</span>
  </div>

  <div class="form-label" style="top:59px">Name<em>*</em></div>
  <div class="field" style="top:74px;height:22px"></div>
  <div class="form-label" style="top:104px">Email<em>*</em></div>
  <div class="field" style="top:119px;height:22px"></div>
  <div class="form-label" style="top:149px">Message<em>*</em></div>
  <div class="field" style="top:164px;height:29px"></div>
</footer>
<div class="btn-send">Send &nbsp;›</div>

<div class="bottom-bar">© Copyright 2014 by Veluna Estates. All rights reserved.
  <div class="social" aria-label="Social links"><span></span><span></span><span></span><span></span><span></span><span></span></div>
</div>

</body>
</html>
```